Velora Multisport Mid Atlantic Region Website Design

Details for my new Wordpress Design Project will be added soon. , What we are looking for:

* The graphic designer will take the following Wordpress template (http://demo.quillaroo.com/lattice/) and create design compositions from it.

* The compositions will need to have a triathlon/multisport look and feel.
We would like the design to have some uniformity with our parent organization: veloramultisport.org

* We need a graphic designer to create compositions for the pages listed below:

A. Homepage

B. News Page (Landing page, which include news categories and featured articles under each category)
i. Individual News Category page
ia. Article Page

C. Events Page (Landing page will display a chronological list of upcoming events)

D. Events listed by specific category
i. Event Details
ii. A calendar view where users can select a particular day of the month
iii. Event list for date selected from calendar view.

F. About Us Page, including the following sub pages:
i. Landing Page (Includes Overview, Mission, and Vision Statement)
ii. Current Council Members
a. Bio page
iii. Current Team Members
a. Bio page (same as one above)

G. Contact Us Page
i. H. Contact Us Form Submission Response Page

NOTE:
* The designer does not need to develop the Wordpress theme from scratch. All initial imagery and PSD’s use will be provided for you.

* Not only will you need to provide each of the above pages as a PSD, all approved icons and other graphics to be used as standalone images will need to be provided as png, jpg and/or gif.

* A Wordpress template we will be provided however the imagery will need to have a look and feel consistent with the spirit of the multisport:

* A detailed requirements document will also be supplied.

* We would like the design to have a similar look as the overseeing body of the Multisport (www.veloramultisport.org), however with some unique appeal.
, Details for my new Wordpress Design Project will be added soon. , What we are looking for:

A. Homepage

ia. Article Page

i. Event Details

a. Bio page
iii. Current Team Members

G. Contact Us Page

NOTE:

```html
<!DOCTYPE html>
<html lang="en">
<head>
<meta charset="utf-8">
<title>Velora Multisport Mid Atlantic Region</title>
<link href="https://fonts.googleapis.com/css2?family=Oswald:wght@400;500;600&family=Open+Sans:wght@400;600;700&display=swap" rel="stylesheet">
<style>
:root{
  --navy:#0b2a5b;
  --navy-dark:#0a1f44;
  --blue:#1f5fb4;
  --link:#1b4f9c;
  --red:#c8102e;
  --text:#333;
  --muted:#666;
  --rule:#dcdcdc;
  --panel:#f2f4f7;
}
*{box-sizing:border-box;margin:0;padding:0}
html,body{width:857px;height:1200px;overflow:hidden;background:#fff}
body{font-family:"Open Sans",Arial,sans-serif;color:var(--text);font-size:8px;line-height:1.45;position:relative}
.site-header{height:72px;display:flex;align-items:center;justify-content:space-between;padding:0 40px 0 30px}
.brand{display:flex;align-items:center;gap:8px;font-family:"Oswald",sans-serif;font-weight:600;font-size:14px;color:var(--navy);line-height:1.05;width:170px}
.brand-dot{width:18px;height:18px;border-radius:50%;background:var(--red);flex:none}
.main-nav{display:flex;align-items:center;gap:18px;font-family:"Oswald",sans-serif;font-size:11px;color:var(--navy);letter-spacing:.5px}
.search{display:flex;gap:4px;margin-left:40px}
.search span{width:92px;height:20px;border:1px solid var(--rule);font-size:8px;color:#999;padding:4px 6px;font-family:"Open Sans",sans-serif}
.search b{height:20px;background:var(--navy);color:#fff;padding:3px 8px;font-weight:500;font-size:10px}
.hero{position:relative;height:285px;background:linear-gradient(100deg,#3d4a2c 0%,#6b7046 30%,#2f3a33 55%,#1b2230 100%)}
.hero-copy{position:absolute;left:470px;top:78px;width:300px;color:#fff}
.hero-kicker{font-family:"Oswald",sans-serif;font-size:14px;color:#7fb2ff;letter-spacing:1px}
.hero-title{font-family:"Oswald",sans-serif;font-size:36px;font-weight:500;line-height:1.05;margin:2px 0 6px}
.hero-copy p{font-size:9.5px;line-height:1.35}
.btn{display:inline-block;background:var(--blue);color:#fff;font-family:"Oswald",sans-serif;font-size:10px;padding:6px 16px;border-radius:2px}
.hero-copy .btn{margin:14px 0 0 90px}
.strip{height:12px;background:var(--navy-dark)}
.content{display:flex;gap:38px;padding:22px 47px 0 50px;height:673px}
.col-main{width:440px}
.col-side{width:282px}
.section-title{font-family:"Oswald",sans-serif;font-size:15px;color:var(--navy);border-bottom:1px solid var(--rule);padding-bottom:4px;margin-bottom:10px}
.section-title em{font-style:normal;color:var(--red)}
.post{display:flex;gap:10px;margin-bottom:10px}
.thumb{background:linear-gradient(135deg,#6d7b8d,#2b3a52);flex:none}
.post .thumb{width:95px;height:70px}
.post h3,.event h3{font-size:8.5px;color:var(--link);font-weight:700}
.more{color:var(--red);font-weight:600;display:block;margin-top:4px}
.member{display:flex;gap:12px;margin-bottom:8px}
.member .thumb{width:140px;height:178px;background:linear-gradient(180deg,#d9d2c8,#9aa6b4)}
.member p,.full p{margin-bottom:6px}
.event{display:flex;gap:8px;padding-bottom:7px;margin-bottom:7px;border-bottom:1px solid var(--rule)}
.event .thumb{width:62px;height:46px}
.date{display:flex;align-items:center;gap:4px;color:var(--red);font-weight:600;font-size:7.5px}
.poll{margin-top:10px;background:var(--panel);border:1px solid var(--rule)}
.poll-head{background:var(--navy);color:#fff;font-family:"Oswald",sans-serif;font-size:14px;padding:8px 10px}
.poll-body{padding:10px}
.poll-q{font-weight:700;color:var(--navy);margin-bottom:8px}
.opt{background:#fff;border:1px solid var(--rule);padding:4px 6px;margin-bottom:5px;display:flex;align-items:center;gap:6px}
.opt i{width:8px;height:8px;border:1px solid #999;border-radius:50%}
.poll .btn{background:var(--red);margin:4px 0 0 170px}
.tweets{height:90px;background:linear-gradient(90deg,#1b3566,#2a4a7d,#1b3566);text-align:center;color:#fff;padding-top:12px}
.tweets h2{font-family:"Oswald",sans-serif;font-size:15px;font-weight:500;display:flex;align-items:center;justify-content:center;gap:12px}
.tweets h2 span{width:60px;height:2px;background:#6ea0e8}
.tweets p{width:560px;margin:8px auto 0;font-size:8.5px}
.site-footer{height:55px;background:var(--navy-dark);color:#c9d3e4;display:flex;align-items:center;justify-content:space-between;padding:0 40px;font-size:8px}
.social{display:flex;gap:8px}
.social i{width:22px;height:22px;border-radius:50%;background:#2f5fae}
</style>
</head>
<body>
<header class="site-header">
  <div class="brand"><span class="brand-dot"></span>Velora Multisport Mid Atlantic Region</div>
  <nav class="main-nav">
    <span>HOME</span><span>NEWS</span><span>EVENTS</span><span>ABOUT</span><span>CONTACT US</span>
    <div class="search"><span>Search here</span><b>Search</b></div>
  </nav>
</header>

<section class="hero" role="img" aria-label="Mountain biker racing across a wooden bridge by a waterfall">
  <div class="hero-copy">
    <div class="hero-kicker">LOREM IPSUM</div>
    <div class="hero-title">SIMPLY DUMMY TEXT</div>
    <p>There are many variations of passages of Lorem Ipsum available but the majority have suffered alteration in some form injected randomised words.</p>
    <span class="btn">Read More</span>
  </div>
</section>
<div class="strip"></div>

<main class="content">
  <div class="col-main">
    <h2 class="section-title"><em>LATEST</em> POST</h2>
    <article class="post">
      <div class="thumb" role="img" aria-label="Athletes at a race start"></div>
      <div><h3>Lorem Ipsum simply dummy</h3><p>Lorem Ipsum is simply dummy text of the printing and typesetting industry. Lorem Ipsum has been the industry's standard dummy text ever since the early days.</p><span class="more">[Read More...]</span></div>
    </article>
    <article class="post">
      <div class="thumb" role="img" aria-label="Cyclists on a road course"></div>
      <div><h3>Lorem Ipsum simply dummy</h3><p>Lorem Ipsum is simply dummy text of the printing and typesetting industry. Lorem Ipsum has been the industry's standard dummy text ever since the early days.</p><span class="more">[Read More...]</span></div>
    </article>

    <h2 class="section-title" style="margin-top:14px"><em>COUNCIL</em> MEMBERS</h2>
    <div class="member">
      <div class="thumb" role="img" aria-label="Portrait of a council member"></div>
      <div>
        <h3 style="font-size:8.5px;color:var(--link)">Lorem Ipsum simply dummy</h3>
        <p>Lorem Ipsum is simply dummy text of the printing and typesetting industry. Lorem Ipsum has been the industry's standard dummy text ever since the 1500s, when an unknown printer took a galley of type and scrambled it to make a type specimen book. It has survived not only five centuries, but also the leap into electronic typesetting, remaining essentially unchanged.</p>
        <p>It was popularised in the 1960s with the release of sheets containing Lorem Ipsum passages, and more recently with desktop publishing software including versions of Lorem Ipsum.</p>
      </div>
    </div>
    <div class="full">
      <p>There are many variations of passages of Lorem Ipsum available, but the majority have suffered alteration in some form, by injected humour, or randomised words which don't look even slightly believable. If you are going to use a passage of Lorem Ipsum, you need to be sure there isn't anything embarrassing hidden in the middle of text.</p>
      <p>Contrary to popular belief, Lorem Ipsum is not simply random text. It has roots in a piece of classical literature from 45 BC, making it over 2000 years old, looked up in the more obscure Latin words and going through the cites of the word in classical literature.</p>
      <span class="more">[Read More...]</span>
    </div>
  </div>

  <aside class="col-side">
    <h2 class="section-title"><em>UPCOMMING</em> EVENTS</h2>
    <div class="event"><div class="thumb" role="img" aria-label="Swimmers in open water"></div><div><div class="date"><svg width="8" height="8" viewBox="0 0 8 8"><rect x=".5" y="1.5" width="7" height="6" fill="none" stroke="#c8102e"/><rect x=".5" y="1.5" width="7" height="2" fill="#c8102e"/></svg>July 12, 2014</div><h3>Lorem Ipsum simply dummy</h3><p>Lorem Ipsum is simply dummy text of the printing industry.</p></div></div>
    <div class="event"><div class="thumb" role="img" aria-label="Runners on a trail"></div><div><div class="date"><svg width="8" height="8" viewBox="0 0 8 8"><rect x=".5" y="1.5" width="7" height="6" fill="none" stroke="#c8102e"/><rect x=".5" y="1.5" width="7" height="2" fill="#c8102e"/></svg>July 19, 2014</div><h3>Lorem Ipsum simply dummy</h3><p>Lorem Ipsum is simply dummy text of the printing industry.</p></div></div>
    <div class="event"><div class="thumb" role="img" aria-label="Cyclist on a climb"></div><div><div class="date"><svg width="8" height="8" viewBox="0 0 8 8"><rect x=".5" y="1.5" width="7" height="6" fill="none" stroke="#c8102e"/><rect x=".5" y="1.5" width="7" height="2" fill="#c8102e"/></svg>July 26, 2014</div><h3>Lorem Ipsum simply dummy</h3><p>Lorem Ipsum is simply dummy text of the printing industry.</p></div></div>
    <div class="event"><div class="thumb" role="img" aria-label="Transition area at a race"></div><div><div class="date"><svg width="8" height="8" viewBox="0 0 8 8"><rect x=".5" y="1.5" width="7" height="6" fill="none" stroke="#c8102e"/><rect x=".5" y="1.5" width="7" height="2" fill="#c8102e"/></svg>Aug 02, 2014</div><h3>Lorem Ipsum simply dummy</h3><p>Lorem Ipsum is simply dummy text of the printing industry.</p></div></div>

    <section class="poll">
      <div class="poll-head">FEATURED POOL</div>
      <div class="poll-body">
        <p class="poll-q">What is the best aspect of the Velora Multisport Mid Atlantic Region for racers?</p>
        <div class="opt"><i></i>Lorem ipsum dolor sit</div>
        <div class="opt"><i></i>Simply dummy text here</div>
        <div class="opt"><i></i>Printer took a galley</div>
        <div class="opt"><i></i>Passages of lorem text</div>
        <span class="btn">SUBMIT POLL</span>
      </div>
    </section>
  </aside>
</main>

<section class="tweets" role="img" aria-label="Faint grid of athlete portraits behind the latest tweet">
  <h2><span></span>LATEST TWEET<span></span></h2>
  <p>@VeloraMulti Lorem ipsum dolor sit amet for our region council members, race organizers and clubs joining the summer series this year. Read the full update online now.</p>
</section>

<footer class="site-footer">
  <span>© 2014 Velora Multisport Mid Atlantic Region. All Rights Reserved.</span>
  <div class="social"><i></i><i></i><i></i></div>
</footer>
</body>
</html>
```